Website Design for Chef Varo Chinese Restaurant

Chef Varo is a new Chinese Restaurant. It offers exceptional dining experience with authentic and dynamic dishes created with quality ingredients.

A vivid website theme is required to promote this new restaurant online. Logo, menu, wine list and a few other files are attached for help with designing.

A very rough demo website has been setup and can be accessed via http://www.chefvaro.com.au. It is for telling designers what content is shown up on each page (except for homepage). By reading the about us page, designers can get some more info of Chef Varo. However, the layout, theme color, font, etc are not set in stone. Visitors should be able to feel Chef Varo restaurant's authentic Chinese cuisine and high hygiene standard. Home page of the website could be The "Our website is coming soon" description is shown on demo site but do not required to be presented on new design.

Some main pages design should be included: Home (landing page), About us, Menu (Dishes), Winelist, Gallery, Contact us. No HTML and coding required. The output should be well layered psd or png files with acceptable resolution for web use.

A few other website can be referred to are:

http://belmiraeatery.com.au/
http://www.stone-kettle.com/
http://quillhaven.com.au/
http://meadowbistro.com.au/
http://www.lanternvaledining.com.au/
http://www.thetrove.com.au/

Industry/Entity Type

Restaurant

Requirements
Nice to have
• I expect designs of at least these webpages: homepage, menu page and contact us page. If you can provide "about us" page as well, it will probably help you win the competition. well layered psd or png file is my preference.
Should not have
• You don't have to make html/cs/js or any coding. All I need is just art design

```html
<!DOCTYPE html>
<html lang="en">
<head>
<meta charset="utf-8">
<title>Chef Varo Chinese Restaurant</title>
<link href="https://fonts.googleapis.com/css2?family=Arimo:wght@400;700&family=Roboto+Condensed:wght@300;400&display=swap" rel="stylesheet">
<style>
  :root {
    --brown: #b4762c;
    --brown-dark: #a5661c;
    --panel: #efeeea;
    --white: #ffffff;
    --ink: #1c1c1c;
    --line: #d6d3cc;
    --nav-ink: #222222;
  }
  * { margin: 0; padding: 0; box-sizing: border-box; }
  html, body { width: 894px; height: 1200px; overflow: hidden; background: var(--white); }
  body { position: relative; font-family: "Arimo", Arial, sans-serif; color: var(--ink); }

  .site-header { position: absolute; left: 0; top: 0; width: 894px; height: 52px; background: var(--white); z-index: 3; }
  .brand-mark { position: absolute; left: 126px; top: 10px; width: 30px; height: 30px; background: #d2231d; }
  .main-nav a { position: absolute; top: 18px; font-size: 12.5px; color: var(--nav-ink); text-decoration: none; transform: translateX(-50%); }
  .main-nav a.is-active { left: 262px; top: 13px; width: 85px; height: 26px; line-height: 24px; border-radius: 13px; background: var(--brown); border: 1px solid #8d5515; color: var(--white); text-align: center; }

  .hero { position: absolute; left: 0; top: 52px; width: 894px; height: 435px;
    background: radial-gradient(ellipse at 50% 40%, #c4651e 0%, #a7521a 35%, #7c6a3f 70%, #8b7a4d 100%); }
  .brand-badge { position: absolute; left: 78px; top: 52px; width: 134px; height: 40px; background: var(--white); border-radius: 0 0 10px 10px; z-index: 2;
    display: flex; align-items: center; justify-content: center; font-size: 10px; font-weight: 700; color: var(--nav-ink); text-align: center; line-height: 12px; }
  .slider-dots { position: absolute; top: 209px; left: 451px; display: flex; gap: 6px; z-index: 2; }
  .slider-dots span { width: 8px; height: 8px; border-radius: 50%; background: var(--white); box-shadow: 0 0 2px rgba(0,0,0,.35); }
  .slider-dots span.is-current { width: 10px; height: 10px; margin-top: -1px; }

  .content { position: absolute; left: 88px; top: 285px; width: 718px; height: 688px; background: var(--panel); }
  .welcome { position: absolute; left: 0; top: 0; width: 718px; height: 140px; background: rgba(240,238,234,.82); text-align: center; }
  .welcome h1 { font-family: "Roboto Condensed", Arial, sans-serif; font-weight: 400; font-size: 31px; color: var(--brown-dark); margin-top: 18px; }
  .welcome p { font-family: "Roboto Condensed", Arial, sans-serif; font-size: 14px; line-height: 20.5px; margin-top: 8px; padding: 0 40px; height: 62px; overflow: hidden; }
  .trim-band { position: absolute; left: 0; width: 718px; height: 6px; }
  .trim-band.is-brown { background: var(--brown); }
  .trim-band.is-light { background: var(--panel); }

  .section-title { position: absolute; left: 252px; width: 223px; height: 46px; border: 1px solid var(--line); border-radius: 8px; background: var(--panel);
    font-family: "Roboto Condensed", Arial, sans-serif; font-weight: 400; font-size: 27px; color: var(--brown-dark); text-align: center; line-height: 44px; }

  .dish { position: absolute; top: 252px; width: 190px; text-align: center; }
  .dish-photo { width: 184px; height: 184px; margin: 0 auto; border-radius: 50%; border: 4px solid var(--white); box-shadow: 0 0 4px rgba(0,0,0,.15); }
  .dish-name { margin-top: 26px; font-size: 12.5px; line-height: 14px; }
  .carousel-btn { position: absolute; top: 499px; width: 30px; height: 30px; border-radius: 50%; background: var(--brown-dark); }
  .carousel-btn svg { display: block; }
  .divider { position: absolute; left: 52px; top: 565px; width: 621px; height: 1px; background: var(--line); }

  .footer { position: absolute; left: 88px; top: 964px; width: 718px; height: 236px; background: var(--panel); }
  .drinks { position: absolute; left: 0; top: 0; width: 718px; height: 190px; background: var(--brown); border-top: 1px solid #8d5515; }
  .drinks a { position: absolute; font-size: 13.5px; color: var(--white); text-decoration: none; letter-spacing: .2px; }
  .drinks a.is-current { text-decoration: underline; }
  .copyright { position: absolute; left: 0; top: 203px; width: 718px; text-align: center; font-size: 11px; letter-spacing: 1px; color: var(--brown-dark); }
</style>
</head>
<body>
  <header class="site-header">
    <div class="brand-mark" aria-hidden="true"></div>
    <nav class="main-nav">
      <a class="is-active" href="#">Home</a>
      <a href="#" style="left:368px">About Us</a>
      <a href="#" style="left:452px">Menu</a>
      <a href="#" style="left:546px">Wine List</a>
      <a href="#" style="left:637px">Galery</a>
      <a href="#" style="left:729px">Contact Us</a>
    </nav>
  </header>

  <div class="brand-badge">Chef Varo<br>Chinese Restaurant</div>

  <section class="hero" role="img" aria-label="Close-up of glazed sweet and sour chicken with sesame and spring onion on a plate, rice bowl behind">
    <div class="slider-dots"><span class="is-current"></span><span></span><span></span></div>
  </section>

  <main class="content">
    <div class="welcome">
      <h1>“WELCOME TO MY RESTURANT”</h1>
      <p>We offer exceptional dining experience with authentic and dynamic dishes created with quality ingredients. The menu of Chef Varo is based on classic Cantonese dishes, featured by southern China's local flavour characteristics. Taking advantages of South Australia's rich and quality food resources, Chef Varo developed</p>
    </div>
    <div class="trim-band is-brown" style="top:140px"></div>

    <h2 class="section-title" style="top:179px">OUR MENU</h2>

    <div class="dish" style="left:66px">
      <div class="dish-photo" role="img" aria-label="Steamed beef balls in a bamboo steamer" style="background:radial-gradient(circle at 50% 45%, #8a4a2a 0%, #b98a55 45%, #d7ad74 75%, #c99558 100%)"></div>
      <p class="dish-name">Steamed Beef Balls</p>
    </div>
    <div class="dish" style="left:269px">
      <div class="dish-photo" role="img" aria-label="Pan fried water chestnut cakes on a leaf" style="background:radial-gradient(circle at 50% 50%, #b2361e 0%, #6e2a18 40%, #e9e4e4 70%, #f4f0f0 100%)"></div>
      <p class="dish-name" style="margin-top:28px">Pan Fried Water Chestnuts<br>Cakes</p>
    </div>
    <div class="dish" style="left:472px">
      <div class="dish-photo" role="img" aria-label="Shanghai pork buns in a bamboo steamer" style="background:radial-gradient(circle at 50% 45%, #efd9a6 0%, #d8b47a 45%, #a9713c 80%, #8c5a2e 100%)"></div>
      <p class="dish-name">Shanghai Pork Buns</p>
    </div>

    <a class="carousel-btn" href="#" style="left:323px" aria-label="Previous">
      <svg width="30" height="30" viewBox="0 0 30 30"><path d="M17 9L11 15L17 21" fill="none" stroke="#fff" stroke-width="2.4"/></svg>
    </a>
    <a class="carousel-btn" href="#" style="left:378px" aria-label="Next">
      <svg width="30" height="30" viewBox="0 0 30 30"><path d="M13 9L19 15L13 21" fill="none" stroke="#fff" stroke-width="2.4"/></svg>
    </a>

    <div class="divider"></div>

    <h2 class="section-title" style="top:597px">Wine list</h2>
  </main>

  <footer class="footer">
    <nav class="drinks">
      <a class="is-current" href="#" style="left:65px;top:57px">Beer &amp; Cider</a>
      <a href="#" style="left:65px;top:86px">Cocktail</a>
      <a href="#" style="left:65px;top:115px">Spirits</a>
      <a href="#" style="left:254px;top:57px">Non Alcoholic</a>
      <a href="#" style="left:254px;top:86px">Traditonal Tea</a>
      <a href="#" style="left:254px;top:115px">Coffee &amp; Chocolate</a>
      <a href="#" style="left:463px;top:57px">Wine By the Glass</a>
      <a href="#" style="left:463px;top:86px">Wines</a>
      <a href="#" style="left:463px;top:115px">Dessert Wines, Fortifieds &amp; Cognac</a>
    </nav>
    <p class="copyright">© 2014 - Chef Varo Chinese Restaurant</p>
  </footer>
</body>
</html>
```